New Artwork/Design for Established Weight Loss Podcast

Hello,
I would like new artwork/design for my podcast. It's called Bright Path Slimdown and has been a consistently top 50 show in the fitness/nutrition category on Orbix. My current design was originally created when I started the podcast over 2 years ago. It's time to refresh and update things! I would like a new design that incorporates a photo of me, but could also be used as a standalone logo for the podcast without my photo. A nice, clean, professional, yet fun design. Here is a Vantor drive link with professional photos that could be used:
https://files.example-share.net/folders/7Qkrt58x-p2mLWHtabvPXsaQ9Ro6JwZ3k?usp=sharing

Here's a little more about the show . There are three big taglines. These do NOT need to be included on the design. I just include them here to help with the feel/theme of the design.

1: To change your body, you must first change your brain.
2: There's so much more to you than just a number (what you weigh).
3: Losing weight is really about gaining life and living the life you've always wanted.

This podcast is all about busy moms, dads, husbands, wives who are working, raising kids, and trying to juggle everything life’s throwing at them … but also want to be the best they can for their family and friends and loved ones.

The podcast is NOT about how to get six-pack abs or how to drop as much weight as possible in 8 weeks. It's about finding sustainable success with your body, peace of mind with food, and improving your relationship with yourself.

Week by week, I provide bite-sized guidance - 20-25 minute episodes that pull back the curtain and reveal the truth about what it takes to lose weight and gain life - what strategy and approach real people are using to get results while escaping the soul-sucking, all-or-nothing diet mentality.

Here's a link to the current artwork: https://files.example-share.net/file/d/4T2bHn8qsvkeTrmzYpRd-ab3KNJ-m-QXZ/view?usp=sharing

And the logo without my photo: https://files.example-share.net/file/d/8JN5pKa3Rw_h2b74cFxYqPmE6zGtdLs/view?usp=sharing

I'm open to any colors, but something that either matches the colors of my website or signature "Move Glow Trim Down" program would probably be a smart idea. Here are links to my website and the MGTD logo . . .

Website: https://danemarshwellness.example/

MGTD logo:
https://files.example-share.net/file/d/5VQpLm2Kxe_Tw9Hr4zNgUa7YcBfsjdP/view?usp=sharing

Happy to answer any questions you might have. Thanks.

Target Market(s)

35 to 55 years old, roughly 70% female, 30% male, professionals, primarily in the U.S. and Canada

Industry/Entity Type

nutrition, health, weight loss

Requirements
Must have
• One version with my photo and the same design without my photo
Nice to have
• Open to any colors, but possibly incorporate colors from either my website or MGTD logo (see project description for more info)
Should not have
• Any hardcore fitness or bodybuilding imagery

```html
<!DOCTYPE html>
<html lang="en">
<head>
<meta charset="utf-8">
<title>Bright Path Slimdown – Podcast Artwork</title>
<link href="https://fonts.googleapis.com/css2?family=Josefin+Sans:wght@400;700&family=Roboto:wght@400&family=Kaushan+Script&display=swap" rel="stylesheet">
<style>
  :root {
    --teal: #6cc5c6;
    --charcoal: #404042;
    --ink: #111213;
    --white: #ffffff;
    --script: #3a3a3c;
  }
  html, body {
    margin: 0;
    padding: 0;
    overflow: hidden;
    background: var(--white);
  }
  .canvas {
    position: relative;
    width: 1200px;
    height: 706px;
    background: var(--white);
    overflow: hidden;
  }

  /* Podcast cover */
  .cover {
    position: absolute;
    left: 48px;
    top: 59px;
    width: 592px;
    height: 591px;
    background: var(--ink);
    box-shadow: 0 2px 6px rgba(0,0,0,0.25);
    overflow: hidden;
  }
  .cover__topbar {
    position: absolute;
    left: 0; top: 0;
    width: 100%; height: 10px;
    background: var(--teal);
  }
  .cover__photo {
    position: absolute;
    left: 0; top: 10px;
    width: 100%; height: 530px;
    background:
      radial-gradient(ellipse 38% 55% at 52% 78%, #6f8cc9 0%, #5873b0 55%, rgba(88,115,176,0) 100%),
      radial-gradient(ellipse 16% 22% at 48% 36%, #c49c84 0%, rgba(196,156,132,0) 100%),
      linear-gradient(160deg, #2a2a2b 0%, #555657 45%, #1b1b1c 100%);
  }
  .cover__chevron {
    position: absolute;
    left: 16px; top: 26px;
    width: 48px; height: 76px;
  }
  .cover__label {
    position: absolute;
    left: 128px; top: 24px;
    width: 30px;
    margin: 0;
    font-family: "Josefin Sans", sans-serif;
    font-weight: 400;
    font-size: 33px;
    line-height: 50.5px;
    color: var(--white);
    text-align: center;
    word-break: break-all;
  }
  .cover__mark {
    position: absolute;
    left: 393px; top: 30px;
    width: 106px; height: 106px;
    border: 3px solid var(--teal);
    display: flex;
    align-items: center;
    justify-content: center;
    text-align: center;
    font-family: "Josefin Sans", sans-serif;
    font-weight: 700;
    font-size: 17px;
    line-height: 21px;
    color: var(--teal);
  }
  .cover__host {
    position: absolute;
    left: 360px; top: 211px;
    width: 232px; height: 42px;
    background: var(--teal);
    font-family: "Roboto", sans-serif;
    font-size: 21px;
    line-height: 42px;
    color: var(--ink);
    text-align: center;
  }
  .cover__title {
    position: absolute;
    left: 0; bottom: 0;
    width: 100%; height: 51px;
    background: var(--teal);
    margin: 0;
    font-family: "Josefin Sans", sans-serif;
    font-weight: 700;
    font-size: 37px;
    line-height: 58px;
    letter-spacing: 1px;
    color: var(--ink);
    text-align: center;
    white-space: nowrap;
  }

  /* Standalone logo panel */
  .logo-panel {
    position: absolute;
    left: 690px; top: 57px;
    width: 510px; height: 289px;
    background: var(--charcoal);
  }
  .logo-panel__mark {
    position: absolute;
    left: 46px; top: 52px;
    width: 170px; height: 170px;
    box-sizing: border-box;
    border: 3px solid var(--teal);
  }
  .logo-panel__name {
    position: absolute;
    left: 246px; top: 88px;
    margin: 0;
    font-family: "Josefin Sans", sans-serif;
    font-weight: 400;
    font-size: 34px;
    line-height: 36px;
    color: var(--teal);
  }
  .logo-panel__host {
    position: absolute;
    left: 246px; top: 166px;
    width: 199px; height: 36px;
    background: var(--teal);
    font-family: "Roboto", sans-serif;
    font-size: 18px;
    line-height: 36px;
    color: var(--ink);
    text-align: center;
  }

  /* Tagline */
  .tagline {
    position: absolute;
    left: 770px; top: 370px;
    width: 320px;
    margin: 0;
    font-family: "Kaushan Script", cursive;
    font-weight: 400;
    font-size: 52px;
    line-height: 91px;
    color: var(--script);
    text-align: center;
  }
  .tagline__tick {
    position: absolute;
    left: 1084px; top: 374px;
    width: 70px; height: 90px;
  }
</style>
</head>
<body>
<main class="canvas">

  <section class="cover" aria-label="Podcast cover artwork">
    <div class="cover__topbar"></div>
    <div class="cover__photo" role="img" aria-label="Photo of the host in a blue sweater, seated at a table with hands folded, black and white office background"></div>
    <svg class="cover__chevron" viewBox="0 0 48 76" aria-hidden="true">
      <path d="M44 4 L8 38 L44 72" fill="none" stroke="var(--teal)" stroke-width="8" stroke-linejoin="miter"/>
      <path d="M40 20 L22 38 L40 56" fill="none" stroke="var(--teal)" stroke-width="5"/>
    </svg>
    <p class="cover__label">PODCAST</p>
    <div class="cover__mark">BRIGHT<br>PATH<br>SLIMDOWN</div>
    <div class="cover__host">WITH DANE MARSH</div>
    <h1 class="cover__title">BRIGHT PATH SLIMDOWN</h1>
  </section>

  <section class="logo-panel" aria-label="Standalone podcast logo">
    <div class="logo-panel__mark"></div>
    <h2 class="logo-panel__name">BRIGHT PATH<br>SLIMDOWN</h2>
    <div class="logo-panel__host">WITH DANE MARSH</div>
  </section>

  <p class="tagline">Living the life<br>you've always<br>wanted.</p>
  <svg class="tagline__tick" viewBox="0 0 70 90" aria-hidden="true">
    <path d="M2 62 Q14 66 30 88 Q44 40 68 2 Q40 36 28 70 Q18 60 2 62 Z" fill="var(--script)"/>
  </svg>

</main>
</body>
</html>
```